QDV Construction and Remodeling

Prefer a matte black card with some colors that pop, but subtle. Contact info. Show General Contractor professional way. Can you please remove renovations repairs maintenance off of my logo.

Target Market(s)

Property and business investors. Homeowners

Industry/Entity Type

Construction

Contact Information for Business Card

Name: Dorian Falkner, Title: CEO, Phone: 555-216-0394, Email: Dorian@QDVbuildTrx.com, website: www QDVbuildTrx.com

Font styles to use
Other font styles liked:
• Designer choose

Colors

Designer to choose colors to be used in the design.

Requirements
Must have
• Uniqueness. Double sided since it wont let me choose that. Professional look, be eye catching and catchy. QR code to my website
Nice to have
• Matte black background, subtle bright colors that pop, but I am open to anything. I also like black and gold with some red. Possible Harborton Ironclad logo colored stars somewhere around the logo or on the back. Just to rep my city
Should not have
• pink. Something you would see somewhere else. gif pictures or generated pictures.

```html
<!DOCTYPE html>
<html lang="en">
<head>
<meta charset="utf-8">
<title>QDV Construction and Remodeling – Business Card</title>
<link rel="stylesheet" href="https://fonts.googleapis.com/css2?family=Montserrat:wght@400;500;700;800&display=swap">
<style>
  :root {
    --backdrop: #c9c9c9;
    --card-black: #141414;
    --gold: #c9a320;
    --gold-deep: #8a6d12;
    --gold-face: #c8a41f;
    --white: #f4f4f4;
  }
  * { margin: 0; padding: 0; box-sizing: border-box; }
  html, body {
    width: 1200px; height: 800px; overflow: hidden;
    background: var(--backdrop);
    font-family: "Montserrat", Arial, sans-serif;
  }
  .stage {
    width: 1200px; height: 800px;
    display: flex; align-items: center; justify-content: center; gap: 40px;
  }
  .card {
    position: relative;
    width: 540px; height: 308px;
    box-shadow: 0 8px 22px rgba(0,0,0,.28);
  }
  .card--front {
    background: var(--card-black);
    border: 2px solid var(--gold);
  }
  .card--back {
    background: var(--gold-face);
    display: flex; align-items: center; justify-content: center;
  }

  /* front: brand block */
  .brand {
    position: absolute; top: 46px; right: 44px;
    display: flex; align-items: center; gap: 12px;
    color: var(--white);
    font-weight: 700;
  }
  .brand__mark {
    width: 14px; height: 14px; background: var(--gold); flex: none;
  }
  .brand__name { line-height: 1.1; font-size: 15px; letter-spacing: .04em; }
  .brand__name .brand__initials { display: block; font-size: 42px; letter-spacing: .02em; }

  /* front: person */
  .person {
    position: absolute; left: 40px; top: 132px;
  }
  .person__name {
    color: var(--gold); font-size: 19px; font-weight: 400;
    text-transform: uppercase; letter-spacing: .03em;
  }
  .person__title {
    color: var(--white); font-size: 12px; font-weight: 500; margin-top: 3px;
  }

  /* front: contact list */
  .contact {
    position: absolute; left: 40px; top: 194px;
    list-style: none; display: flex; flex-direction: column; gap: 6px;
  }
  .contact__item {
    display: flex; align-items: center; gap: 8px;
    color: var(--white); font-size: 13px; font-weight: 500;
  }
  .contact__item .accent { color: var(--gold); }
  .contact__icon { width: 13px; height: 13px; flex: none; }

  /* front: role band */
  .role {
    position: absolute; left: 30px; right: 30px; bottom: 22px;
    display: flex; align-items: center; gap: 12px;
  }
  .role__rule { flex: 1; height: 1px; background: var(--gold); }
  .role__rule--short { flex: 0 0 150px; }
  .role__label {
    color: var(--gold); font-size: 17px; font-weight: 800;
    letter-spacing: .1em; text-transform: uppercase; white-space: nowrap;
  }
  .top-rule {
    position: absolute; left: 230px; right: 30px; top: 118px;
    height: 1px; background: var(--gold);
  }

  /* back */
  .back-brand {
    display: flex; align-items: center; gap: 16px;
    color: var(--gold-deep); font-weight: 700;
  }
  .back-brand__mark { width: 20px; height: 20px; background: var(--gold-deep); }
  .back-brand__name { font-size: 20px; line-height: 1.1; letter-spacing: .04em; }
  .back-brand__name .brand__initials { display: block; font-size: 64px; letter-spacing: .02em; }
</style>
</head>
<body>
<main class="stage">

  <section class="card card--front" aria-label="Card front">
    <div class="brand">
      <span class="brand__mark"></span>
      <span class="brand__name"><span class="brand__initials">QDV</span>Construction and Remodeling</span>
    </div>

    <div class="top-rule"></div>

    <div class="person">
      <p class="person__name">Dorian Falkner</p>
      <p class="person__title">CEO</p>
    </div>

    <ul class="contact">
      <li class="contact__item">
        <svg class="contact__icon" viewBox="0 0 24 24" aria-hidden="true"><path fill="#c9a320" d="M6.6 10.8a15.1 15.1 0 0 0 6.6 6.6l2.2-2.2c.3-.3.7-.4 1-.2 1.1.4 2.3.6 3.6.6.6 0 1 .4 1 1V20c0 .6-.4 1-1 1A17 17 0 0 1 3 4c0-.6.4-1 1-1h3.5c.6 0 1 .4 1 1 0 1.3.2 2.5.6 3.6.1.3 0 .7-.2 1z"/></svg>
        555-216-0394
      </li>
      <li class="contact__item">
        <svg class="contact__icon" viewBox="0 0 24 24" aria-hidden="true"><path fill="#c9a320" d="M2 5h20v14H2z"/><path fill="none" stroke="#141414" stroke-width="1.8" d="M2 5l10 8 10-8"/></svg>
        Dorian@QDVbuildTrx.com
      </li>
      <li class="contact__item">
        <svg class="contact__icon" viewBox="0 0 24 24" aria-hidden="true"><circle cx="12" cy="12" r="10" fill="#c9a320"/><path fill="none" stroke="#141414" stroke-width="1.4" d="M2 12h20M12 2c3 3 3 17 0 20M12 2c-3 3-3 17 0 20M4 7h16M4 17h16"/></svg>
        <span>www.<span class="accent">QDVbuildTrx.com</span></span>
      </li>
    </ul>

    <div class="role">
      <span class="role__rule role__rule--short"></span>
      <span class="role__label">General Contractor</span>
      <span class="role__rule"></span>
    </div>
  </section>

  <section class="card card--back" aria-label="Card back">
    <div class="back-brand">
      <span class="back-brand__mark"></span>
      <span class="back-brand__name"><span class="brand__initials">QDV</span>Construction and Remodeling</span>
    </div>
  </section>

</main>
</body>
</html>
```